Automotive component supplier needs a business card design

We need a business card design for our company called Velmar Global Components Ltd based in the UK. We are a supplier of interior and exterior components to premium car manufacturers such as Corvane Hale, Durrant Fyfe, Maxtorn and Valdessimo. We would like to see a modern business card design that uses the colour blue.

Target Market(s)

Premium automotive car manufacturers.

Industry/Entity Type

Automotive

Contact Information for Business Card

Company Name : Velmar Global Components Limited
Address: 17 Tamsey Yard, Upper Drisk, Warwick, CV31 8RJ, United Kingdom
Web Address : www.velmarparts-example.co.uk

Font styles to use
Other font styles liked:
• Helvetica

Colors
3176b5
0255a3
85acd3
cfdeed
cee9f5
85cae6
34a6d7
0692cd
9bcb3c

Requirements
Must have
• Clear company logo and a mixture of blue colours.
Nice to have
• A high quality modern image.
Should not have
• Multiple colours.

```html
<!DOCTYPE html>
<html lang="en">
<head>
<meta charset="utf-8">
<title>Velmar Global Components – Business Card</title>
<link href="https://fonts.googleapis.com/css2?family=Arimo:wght@400;700&display=swap" rel="stylesheet">
<style>
  :root {
    --page-bg: #ecedef;
    --card-front: #0a8fcc;
    --card-back: #23272a;
    --brand-blue: #0692cd;
    --light-blue: #34a6d7;
    --accent-green: #9bcb3c;
    --white: #ffffff;
  }
  * { margin: 0; padding: 0; box-sizing: border-box; }
  html, body {
    width: 1200px; height: 780px; overflow: hidden;
    background: var(--page-bg);
    font-family: "Arimo", Helvetica, Arial, sans-serif;
  }
  .sheet {
    width: 1200px; height: 780px;
    display: flex; align-items: center; justify-content: center; gap: 40px;
  }
  .card {
    width: 540px; height: 309px; position: relative;
    border-radius: 2px;
    box-shadow: 0 6px 18px rgba(0,0,0,.18);
  }
  .card--front {
    background: var(--card-front);
    display: flex; align-items: center; justify-content: center;
  }
  .wordmark { display: flex; flex-direction: column; align-items: flex-start; font-weight: 700; }
  .wordmark__name { font-size: 74px; letter-spacing: 2px; line-height: 1; }
  .wordmark__tag { font-size: 14px; letter-spacing: 2.4px; margin-top: 6px; }
  .card--front .wordmark { color: var(--white); }

  .card--back { background: var(--card-back); display: flex; align-items: center; }
  .card--back .wordmark { color: var(--brand-blue); margin-left: 34px; }
  .card--back .wordmark__name { font-size: 50px; letter-spacing: 1.5px; }
  .card--back .wordmark__tag { font-size: 9.5px; letter-spacing: 1.7px; margin-top: 5px; }

  .divider {
    width: 1px; height: 170px; background: var(--accent-green);
    margin: 0 26px 0 30px;
  }
  .details { color: var(--light-blue); font-size: 11.5px; line-height: 1.38; }
  .details__name { font-weight: 700; font-size: 15px; letter-spacing: .5px; color: var(--brand-blue); }
  .details__role { color: var(--accent-green); font-size: 12px; margin-bottom: 6px; }
  .details__address { margin-bottom: 8px; }
  .contact-list { list-style: none; }
  .contact-list li { display: flex; align-items: center; gap: 6px; margin-bottom: 2px; }
  .contact-list svg { width: 13px; height: 13px; flex: none; }
</style>
</head>
<body>
<main class="sheet">
  <section class="card card--front" aria-label="Card front">
    <div class="wordmark">
      <span class="wordmark__name">VELMAR</span>
      <span class="wordmark__tag">GLOBAL COMPONENTS</span>
    </div>
  </section>

  <section class="card card--back" aria-label="Card back">
    <div class="wordmark">
      <span class="wordmark__name">VELMAR</span>
      <span class="wordmark__tag">GLOBAL COMPONENTS</span>
    </div>
    <div class="divider"></div>
    <div class="details">
      <p class="details__name">EMPLOYEE NAME</p>
      <p class="details__role">Managing Director</p>
      <p class="details__address">17 Tamsey Yard, Upper Drisk<br>Warwick, CV31 8RJ<br>United Kingdom</p>
      <ul class="contact-list">
        <li>
          <svg viewBox="0 0 13 13" aria-hidden="true"><rect width="13" height="13" rx="2" fill="#9bcb3c"/><rect x="4" y="2" width="5" height="9" rx="1" fill="#23272a"/></svg>
          (01) 9087 4412
        </li>
        <li>
          <svg viewBox="0 0 13 13" aria-hidden="true"><rect width="13" height="13" rx="2" fill="#9bcb3c"/><path d="M3 4.5c0-1 1-2 3.5-2S10 3.5 10 4.5l-1.5 1-1-1h-2l-1 1z" fill="#23272a"/><rect x="3" y="7" width="7" height="3.5" rx="1" fill="#23272a"/></svg>
          (01) 9087 4413
        </li>
        <li>
          <svg viewBox="0 0 13 13" aria-hidden="true"><rect width="13" height="13" rx="2" fill="#9bcb3c"/><rect x="2.5" y="3.5" width="8" height="6" fill="none" stroke="#23272a" stroke-width="1.2"/><path d="M2.5 3.5l4 3.2 4-3.2" fill="none" stroke="#23272a" stroke-width="1.2"/></svg>
          hello@velmar-example.co.uk
        </li>
        <li>
          <svg viewBox="0 0 13 13" aria-hidden="true"><rect width="13" height="13" rx="6.5" fill="#9bcb3c"/><circle cx="6.5" cy="6.5" r="3.8" fill="none" stroke="#23272a" stroke-width="1.1"/><path d="M2.7 6.5h7.6M6.5 2.7c-2 2.5-2 5.1 0 7.6M6.5 2.7c2 2.5 2 5.1 0 7.6" fill="none" stroke="#23272a" stroke-width=".9"/></svg>
          www.velmarparts-example.co.uk
        </li>
      </ul>
    </div>
  </section>
</main>
</body>
</html>
```